Massage Therapy and Energy Healing Practice

I am a massage therapist, Reiki energy healer, I sell herbs and oils, and also a health lifestyle coach. I need a design that is strong because I'm not a spa. I do therapeutic work, but I want a touch of the energy and spiritual healing I do as well to be included in the design. I like blue, green, or purple colors. I live in the Blue Ridge Mountains of VA and even though my practice is in the city I like my love for nature and the earth to show through. I would like a single image logo so I can use the image many places. I need a strong brand that will let others know that I combine massage therapy in a therapeutic way while keeping my touches of energy healing, nurturing, herb crafting, and mother earth loving ways.
Updates

Just some things about me:I like to hike. I live on a farm. I own horses, cows, sheep and dogs. I love nature and the energy in produces. I'm very spiritual. I don't know how these things might help or if they do, but I know that my personality might help inspire what I will find good in a design. Added Sunday, December 13, 2015

Target Market(s)

People in pain. People who need spiritual council. Need herbal medicine advice. Holistic healthcare.

Industry/Entity Type

Massage

Contact Information for Business Card

Kneadwell Harbor
Norah T. Lindqvist C.M.T, R.M.T
40913 Hollister Creek Court, Dunmore, VA
540-718-2263

Colors
3176b5
85abd2
876aae
9bcb3c

Requirements
Must have
• Strong Branding that promotes my massage therapy practice first
Nice to have
• Something to evoke my herbal medicine, my energy healing, my spiritual side

```html
<!DOCTYPE html>
<html lang="en">
<head>
<meta charset="utf-8">
<title>Kneadwell Harbor — Business Card</title>
<link href="https://fonts.googleapis.com/css2?family=Libre+Bodoni:wght@400&family=Arimo:wght@400&display=swap" rel="stylesheet">
<style>
  :root {
    --page-bg: #e9e6e1;
    --card-bg: #ffffff;
    --ink: #1a1a1a;
    --leaf: #8cc63f;
    --meadow-light: #a9cf6a;
    --meadow-deep: #5f8f2c;
    --fleece: #e8e2d3;
  }
  * { margin: 0; padding: 0; box-sizing: border-box; }
  html, body {
    width: 1200px;
    height: 892px;
    overflow: hidden;
    background: var(--page-bg);
  }
  .business-card {
    position: absolute;
    left: 100px;
    top: 160px;
    width: 1000px;
    height: 572px;
    background: var(--card-bg);
    box-shadow: 0 10px 30px rgba(0,0,0,0.18);
    overflow: hidden;
  }
  .card-art {
    position: absolute;
    inset: 0;
    width: 1000px;
    height: 572px;
  }
  .brand-name {
    position: absolute;
    right: 40px;
    top: 40px;
    font-family: "Libre Bodoni", "Bodoni Moda", serif;
    font-size: 50px;
    font-weight: 400;
    color: var(--ink);
    letter-spacing: 0.5px;
  }
  .therapist {
    position: absolute;
    left: 560px;
    top: 150px;
    font-family: "Arimo", Arial, sans-serif;
    color: var(--ink);
  }
  .therapist-name {
    font-size: 40px;
    font-weight: 400;
  }
  .therapist-credentials {
    margin-top: 14px;
    margin-left: 80px;
    font-size: 26px;
    letter-spacing: 1px;
  }
  .contact {
    position: absolute;
    right: 40px;
    bottom: 40px;
    font-family: "Arimo", Arial, sans-serif;
    color: var(--ink);
    font-size: 26px;
    text-align: right;
    line-height: 1.55;
  }
  .contact-phone { margin-right: 150px; }
</style>
</head>
<body>
  <section class="business-card">
    <svg class="card-art" viewBox="0 0 1000 572" xmlns="http://www.w3.org/2000/svg">
      <defs>
        <linearGradient id="meadow" x1="0" y1="0" x2="0" y2="1">
          <stop offset="0" stop-color="var(--fleece)"/>
          <stop offset="0.45" stop-color="var(--meadow-light)"/>
          <stop offset="1" stop-color="var(--meadow-deep)"/>
        </linearGradient>
      </defs>
      <path class="meadow-photo" role="img" aria-label="Photograph of sheep standing in tall green grass"
            d="M0,0 H515 C565,200 545,420 420,572 H0 Z" fill="url(#meadow)"/>
      <path class="leaf-swoosh" d="M515,0 C565,200 545,420 420,572"
            fill="none" stroke="var(--leaf)" stroke-width="12"/>
    </svg>

    <h1 class="brand-name">Kneadwell Harbor</h1>

    <div class="therapist">
      <p class="therapist-name">Norah T. Lindqvist</p>
      <p class="therapist-credentials">C.M.T, R.M.T</p>
    </div>

    <div class="contact">
      <p class="contact-phone">540-718-2263</p>
      <p class="contact-address">40913 Hollister Creek Court, Dunmore, VA</p>
    </div>
  </section>
</body>
</html>
```